Lending Harbor Partners - business cards

we need new business cards for my company.
i've been in business for 25 years.
my wife and I are mortgage brokers.

we just bought the domain for a website with www.homekeyfunding.example
that could be used in the design also.

On the business card would be
Front card:

Dale Whitcomb
Owner/Loan Officer
Cell: (555) 314-2297
Lending Harbor Partners
4172 Pinecrest Lane
Alder Springs, CA 99999
Office (555) 490-6631
Fax (555) 490-6674
website www.homekeyfunding.example

Back of Card:

LHP BRE #0378215 NMLS #586249
Dale Whitcomb BRE # 04519863 NMLS #587716

Industry/Entity Type

Business

```html
<!DOCTYPE html>
<html lang="en">
<head>
<meta charset="utf-8">
<title>Lending Harbor Partners – Business Cards</title>
<link rel="stylesheet" href="https://fonts.googleapis.com/css2?family=Open+Sans:wght@400;600&display=swap">
<style>
  :root {
    --backdrop: #e9e7e3;
    --card: #ffffff;
    --navy: #1c4f7c;
    --rust: #c0622a;
    --ink: #3a3a3a;
    --muted: #6b6b6b;
    --shadow: rgba(0,0,0,0.14);
  }
  * { margin: 0; padding: 0; box-sizing: border-box; }
  html, body { width: 1200px; height: 918px; overflow: hidden; }
  body {
    background: var(--backdrop);
    font-family: "Open Sans", sans-serif;
    color: var(--ink);
    display: flex;
    flex-direction: column;
    align-items: center;
    justify-content: center;
    gap: 38px;
  }
  .card {
    width: 700px;
    height: 400px;
    background: var(--card);
    box-shadow: 0 6px 22px var(--shadow);
    position: relative;
  }
  .brand {
    display: flex;
    align-items: center;
    gap: 10px;
    color: var(--navy);
    font-weight: 600;
    font-size: 22px;
    letter-spacing: 0.5px;
    text-transform: uppercase;
    white-space: nowrap;
  }
  .brand-mark { width: 14px; height: 14px; background: var(--rust); flex: none; }

  /* Front */
  .card-front { display: flex; }
  .front-brand-side {
    width: 52%;
    display: flex;
    align-items: center;
    justify-content: center;
  }
  .front-brand-side .brand { font-size: 19px; }
  .divider {
    position: absolute;
    left: 52%;
    top: 24px;
    bottom: 24px;
    width: 1px;
    background: var(--rust);
  }
  .front-details { flex: 1; padding: 52px 0 0 30px; }
  .person-name { color: var(--navy); font-size: 29px; font-weight: 600; line-height: 1.1; }
  .person-title { color: var(--ink); font-size: 16px; margin-top: 4px; }
  .contact-row { display: flex; gap: 14px; margin-top: 26px; font-size: 15.5px; line-height: 1.35; }
  .contact-row + .contact-row { margin-top: 18px; }
  .contact-icon { width: 18px; height: 18px; flex: none; margin-top: 1px; fill: var(--navy); }
  .contact-icon.is-outline { fill: none; stroke: var(--navy); stroke-width: 1.4; }

  /* Back */
  .card-back {
    display: flex;
    flex-direction: column;
    align-items: center;
    justify-content: center;
    gap: 46px;
  }
  .licences { text-align: center; font-size: 15px; color: var(--muted); line-height: 1.6; }
</style>
</head>
<body>
  <section class="card card-front" aria-label="Business card front">
    <div class="front-brand-side">
      <div class="brand"><span class="brand-mark"></span>Lending Harbor Partners</div>
    </div>
    <div class="divider"></div>
    <div class="front-details">
      <h1 class="person-name">Dale Whitcomb</h1>
      <p class="person-title">Owner/Loan Officer</p>

      <div class="contact-row">
        <svg class="contact-icon" viewBox="0 0 20 20" aria-hidden="true"><path d="M10 2 1 10h3v8h4.5v-5h3v5H16v-8h3z"/></svg>
        <p>Lending Harbor Partners<br>4172 Pinecrest Lane<br>Alder Springs, CA 99999</p>
      </div>
      <div class="contact-row">
        <svg class="contact-icon" viewBox="0 0 20 20" aria-hidden="true"><path d="M2 6c0-2 3-3 8-3s8 1 8 3v2h-4V6.5c-1-.4-2.5-.6-4-.6s-3 .2-4 .6V8H2zm3 3h10l2 8H3z"/></svg>
        <p>Cell: (555) 314-2297<br>Office: (555) 490-6631<br>Fax: (555) 490-6674</p>
      </div>
      <div class="contact-row">
        <svg class="contact-icon is-outline" viewBox="0 0 20 20" aria-hidden="true"><circle cx="10" cy="10" r="8"/><ellipse cx="10" cy="10" rx="3.5" ry="8"/><path d="M2 10h16M3.5 6h13M3.5 14h13"/></svg>
        <p>www.homekeyfunding.example</p>
      </div>
    </div>
  </section>

  <section class="card card-back" aria-label="Business card back">
    <div class="brand"><span class="brand-mark"></span>Lending Harbor Partners</div>
    <div class="licences">
      <p>LHP BRE #0378215 NMLS #586249</p>
      <p>Dale Whitcomb BRE # 04519863 NMLS #587716</p>
    </div>
  </section>
</body>
</html>
```